Men's Health Coaching Business - UK based

I am a UK based Health Coach who requires a clean Word Press 'lifestyle' design. The website will be a window to my services and is not intended to be a place to hang volumes of information off. It needs to be professional looking but with a hint of fun; easy/fun to navigate, intuitive and pleasing to the eye.

The site needs to be image/icon/video based to attract potential clients to my health coaching service. it should also encompass a creative/strong 'Call to Action' throughout the site - i.e. 'contact me'. I will only be using Circlebook and ProLinks for social media. Please also consider the colours of the beach/ocean and other lifestyle images I intend to you.

Images in your submission:

I am doing a photoshoot in July/Aug and so there is no need seek 'ideal images' as I will have a personal catalogue to choose from - examples along the lines of the above brief will be fine in your submission.

Good luck, I look forward to your submissions. Thank you.

Target Market(s)

My target audience is successful/professional men aged 30+ who are likely to lead busy lives, Dads, and enjoy hobbies/activities that keep them fit and healthy. They are probably cash-rich but time-poor - hence the clean, intuitive requirement for the site. I am also male who has a family. I require the site to have a slightly more masculine look/feel to it i.e. font, shapes etc. It must also compliment my logo coaching philosophy (see below).

Industry/Entity Type

Health

Font styles to use
Sans Serif

Colors

Designer to choose colors to be used in the design.

Requirements
Must have
• I have uploaded my logo for reference and inspiration and some images that are similar to the those that will be used throughout the site. The concept is below, but please feel free to employ your 'creative genius' to how it will operate/look/work; In broad terms, I require the following:
• 1 (Home Page): This will need to strongly convey the 'Why' to clients using my services by 1. showcasing who I am (My Story) through a Vimeo/Youtube; 2. showing results of previous clients through an eye-catching testimonials section; and 3. conveying to clients (as creatively as possible) the comprehensive approach of my coaching business; through the following elements (if this can be represented through an eye-catching graphic that chimes with my logo - even better):
• - Nutrition
• - Exercise
• - Mental well-being
• - Sleep - adequate/quality
• - Play - rest and recuperation
• - Sunlight - adequate
• - Plan, execute, review
• 2. 'My Philosophy' page: This will contain a number of paragraphs outlining to potential clients my guiding principles. The headings for each paragraph are:
• - I empathise - I'm a busy family man.
• - I choose my clients extremely carefully.
• - I guide, you decide.
• - I give it to you straight.
• - I give you the tools to change, build great health and see results.
• - If you don't fully commit, we'll part company.
• - I'm evidence-based and results driven.
• - I trust the numbers.
• - Consistency over perfection.
• - I take a comprehensive approach.
• - Guiding principles, not a prescriptive programme.
• - I will recommend some products - I don't sell them.
• - I use technology when it's complimentary.
• - Exercise is important but it's not the only factor.
• - I keep it simple for success.
• - I incorporate interventions that give you the biggest bang for your buck.
• - My guidance is designed to blend with your life.
• - I take a layered and progressive approach.
• - We'll have fun with the process.
• On the philosophy page, the images will be more atuned to preparing meals with the kids in the kitchen and images depicting other aspects of the key pillars such as Play - games with the kids, hobbies, activities or sports; rest and recuperation (reading, holidays etc); and using your brain.
• 3. The 'Investment' page (my prices page). This page needs to show three different packages: Bronze, Silver and Gold. An editable info-graph for ease of readability and showing what the client gets for each package/cost.
• Page 4. The 'Project You' Page. This page will show the client journey; ideally, icon/graphic driven, it should show a typical journey for a client, incorporating the following (taken from the Bronze Package) - please make this quick and fun to view:
• - Meet-up: coffee shop, telephone/video call.
• - Client completes e-Questionnaire.
• - Client records a 'typical week' in a journal.
• - Analyse/discuss e-Questionnaire with the client.
• - Analyse/discuss journal with the client.
• - Testing - Health Markers.
• - Testing - Body Composition Measurement.
• - Fitness Testing (if required) - tailored to sport/activity and preference.
• - Intervention Design and Refine.
• - Clients keep a journal of progress + supporting Meet/Video/telephone consultations.
• - 3-month: re-testing of Health Markers, Body Composition and Fitness.
• The Silver and Gold packages incorporate further testing and interventions as required.
• Page 5. The 'Exercise Sessions' page - VLOG. This page will hold a catalogue of home-based exercise films via Vimeo/Youtube for clients to use/refer to/follow anytime/anywhere. For each post/session I require a template that (as creatively as possible) can:
• - Hold a video;
• - Incorporate an editable info-graph that allows me to the following information fixed information.
• - Session title (header)
• - Exercise names (a maximum of 4 for each clip)
• Against each exercise I need to be able to show some or all of the following information - preferably icon/minimum words driven:
• - Intensity (i.e. low, medium, high, maximum)
• - Coaching points (be able to list of 4-5 key coaching points).
• - Safety points (to be able to list 4-5 key safety points).
• - Session goal (i.e. Strength, CV fitness; movement competency etc).
• - Session - Total time
• - Target heart rate during work (i.e. 150-160bpm)
• - Equipment options (i.e. bodyweight, kettle bell, power-bag, weighted bar, Olympic bar etc)
• - Sets.
• - Reps per set (i.e. 15 reps).
• - Duration per set (i.e. 30s).
• - Block sets (i.e. 3 x 3 sets)
• - Rest between sets (i.e. 30s)
• - Rest between block sets (i.e. 2 min)
• - Tempo (i.e. 2s-1s-3s)
• - Interval ratio (i.e. 30s work/10s rest)
• - Recover heart rate target (i.e. 120bpm)
• Viewable on other devices with no change in format.
Nice to have
• Whilst I need it to be professional, a little humour (design, quotes) would be great...
Should not have
• The look I definitely don't want - Bootcamp; gym/personal trainer; corporate; consultancy; feminine; flowery; fashion; cartoon; cluttered and confusing.

```html
<!DOCTYPE html>
<html lang="en">
<head>
<meta charset="utf-8">
<title>Rob Calder Health Coach</title>
<link rel="stylesheet" href="https://fonts.googleapis.com/css2?family=Montserrat:wght@400;500;600;700&family=Arimo:wght@400;700&display=swap">
<style>
:root{
  --teal:#17a89c;
  --teal-band:#14a99a;
  --ink:#333333;
  --muted:#6e6e6e;
  --light:#f4f5f6;
  --white:#ffffff;
  --footer:#231f20;
  --rule:#3c3839;
  --star:#f2b01e;
}
*{margin:0;padding:0;box-sizing:border-box}
html,body{width:1200px;height:2667px;overflow:hidden;background:var(--white)}
body{position:relative;font-family:"Arimo",Arial,sans-serif;color:var(--ink)}
.abs{position:absolute}
.heading{font-family:"Montserrat",Arial,sans-serif;font-weight:500;color:var(--teal);letter-spacing:.5px;font-size:25px}
.center{text-align:center}
.body-text{font-size:11.5px;line-height:23px;color:var(--muted)}
.btn{position:absolute;background:var(--teal);color:var(--white);font-family:"Montserrat",Arial,sans-serif;font-weight:600;font-size:15px;display:flex;align-items:center;justify-content:center;letter-spacing:.5px}

/* header */
.site-header{position:absolute;left:0;top:0;width:1200px;height:96px;background:var(--white);z-index:3;box-shadow:0 1px 3px rgba(0,0,0,.08)}
.brand-badge{position:absolute;left:85px;top:-30px;width:146px;height:206px;border-radius:0 0 73px 73px;background:var(--white);z-index:4;display:flex;flex-direction:column;align-items:center;padding-top:92px}
.brand-name{display:flex;align-items:center;gap:7px;font-family:"Montserrat",Arial,sans-serif;font-weight:600;font-size:19px;color:var(--ink);letter-spacing:1px;white-space:nowrap}
.brand-square{width:10px;height:10px;background:var(--teal)}
.brand-sub{font-family:"Montserrat",Arial,sans-serif;font-weight:600;font-size:9px;color:var(--ink);letter-spacing:3px;margin-top:5px}
.main-nav{position:absolute;top:44px;left:0;width:1200px;font-family:"Montserrat",Arial,sans-serif;font-size:12.5px;color:#777}
.main-nav span{position:absolute;white-space:nowrap}
.main-nav .active{color:var(--teal);font-weight:600}

/* hero */
.hero{position:absolute;left:0;top:96px;width:1200px;height:549px;background:linear-gradient(180deg,#a9b4ba 0%,#d8d1bf 30%,#6d8a97 52%,#2f5364 75%,#1f3b49 100%)}
.hero-panel{position:absolute;left:708px;top:144px;width:435px;height:276px;background:rgba(70,70,70,.72)}
.hero-title{position:absolute;left:30px;top:22px;font-family:"Montserrat",Arial,sans-serif;color:var(--white);font-size:25px;line-height:40px;font-weight:500;letter-spacing:.5px}
.hero-title .big{font-weight:400;font-size:29px;letter-spacing:1px}
.hero-copy{position:absolute;left:30px;top:110px;width:385px;font-size:11px;line-height:20px;color:#eee}
.hero-dots{position:absolute;left:335px;top:240px;display:flex;gap:9px}
.hero-dots i{width:14px;height:14px;border:2px solid var(--white);border-radius:50%}
.hero-dots i.on{background:var(--teal);border-color:var(--teal)}

/* who i am */
.video{position:absolute;left:590px;top:697px;width:524px;height:341px;background:linear-gradient(160deg,#8ea6b8 0%,#c9c1b3 45%,#b09073 75%,#7a6552 100%)}
.video-bar{position:absolute;left:0;bottom:0;width:100%;height:22px;background:#1b1b1b;color:#ddd;font-size:9px;display:flex;align-items:center;padding-left:12px;gap:14px}
.video-bar::before{content:"";position:absolute;left:0;top:0;width:6px;height:3px;background:#c00}

/* services */
.services{position:absolute;left:0;top:1097px;width:1200px;height:480px;background:var(--light)}
.service{position:absolute;top:126px;width:251px}
.service-photo{width:251px;height:168px}
.service-title{margin-top:22px;font-family:"Montserrat",Arial,sans-serif;font-weight:600;color:var(--teal);font-size:16px;text-align:center;letter-spacing:.5px}
.service-copy{margin-top:12px;font-size:11.5px;line-height:23px;color:var(--muted);text-align:center;padding:0 10px}

/* why choose */
.why{position:absolute;left:0;top:1577px;width:1200px;height:403px;background:linear-gradient(90deg,rgba(20,169,154,.96),rgba(28,176,160,.9)),#4aa6a0;color:var(--white)}
.pillar{position:absolute;top:170px;width:200px;text-align:center}
.pillar-ring{width:110px;height:110px;border:2.5px solid var(--white);border-radius:50%;margin:0 auto;display:flex;align-items:center;justify-content:center}
.pillar-label{margin-top:17px;font-family:"Montserrat",Arial,sans-serif;font-weight:500;font-size:15px;line-height:24px;letter-spacing:.5px}

/* testimonials */
.testimonial{position:absolute;top:2137px;width:320px}
.avatar{position:absolute;left:0;top:0;width:88px;height:88px;border-radius:50%;border:3px solid #ddd;background:linear-gradient(180deg,#c9c4bd,#8f8a84)}
.quote{position:absolute;left:107px;top:5px;width:215px;font-size:11.5px;line-height:22px;color:var(--muted)}
.quote b{font-family:Georgia,serif;font-size:18px;color:#999;font-style:italic;margin-right:6px}
.t-name{position:absolute;left:107px;top:117px;font-family:"Montserrat",Arial,sans-serif;font-weight:700;color:var(--teal);font-size:11.5px}
.t-date{position:absolute;left:107px;top:140px;font-size:11px;color:var(--ink)}
.t-stars{position:absolute;left:107px;top:159px}

/* footer */
.site-footer{position:absolute;left:0;top:2357px;width:1200px;height:310px;background:var(--footer);color:var(--white)}
.foot-brand{position:absolute;left:70px;top:110px;width:240px;display:flex;flex-direction:column;align-items:center}
.foot-brand-name{display:flex;align-items:center;gap:12px;font-family:"Montserrat",Arial,sans-serif;font-weight:500;font-size:32px;letter-spacing:2px;white-space:nowrap}
.foot-brand-square{width:16px;height:16px;background:var(--teal)}
.foot-brand-sub{margin-top:8px;font-family:"Montserrat",Arial,sans-serif;font-weight:500;font-size:12px;letter-spacing:4px}
.foot-heading{position:absolute;top:44px;font-family:"Montserrat",Arial,sans-serif;font-weight:600;font-size:16.5px;letter-spacing:.5px}
.foot-text{position:absolute;font-size:12px;line-height:20px;color:#eee}
.contact-row{position:absolute;left:383px;font-size:11.5px;display:flex;gap:14px;align-items:flex-start;line-height:17px}
.email-field{position:absolute;left:651px;top:137px;width:229px;height:32px;background:var(--white);color:#777;font-size:11.5px;padding-left:12px;display:flex;align-items:center}
.social{position:absolute;left:921px;top:170px;display:flex;gap:18px;font-size:12px}
.social-item{display:flex;align-items:center;gap:7px}
.social-dot{width:20px;height:20px;border:1.5px solid var(--white);border-radius:50%}
</style>
</head>
<body>

<header class="site-header">
  <nav class="main-nav">
    <span class="active" style="left:468px">HOME</span>
    <span style="left:553px">MY PHILOSOPHY</span>
    <span style="left:702px">THE &nbsp;INVESTMENT</span>
    <span style="left:858px">PROJECT YOU</span>
    <span style="left:990px">EXERCISE SESSIONS</span>
  </nav>
</header>
<div class="brand-badge">
  <div class="brand-name"><span class="brand-square"></span>ROB CALDER</div>
  <div class="brand-sub">HEALTH COACH</div>
</div>

<section class="hero" role="img" aria-label="Photo: a man kneeling on a paddle board at sea at sunset">
  <div class="hero-panel">
    <h1 class="hero-title">MEN'S HEALTH<br><span class="big">COACHING BUSINESS</span></h1>
    <p class="hero-copy">Sed ut perspiciatis unde omnis iste natus error sit voluptatem accusantium doloremque laudantium, totam rem aperiam, eaque ipsa quae quasi architecto beatae vitae dicta sunt explicabo.</p>
    <div class="btn" style="left:35px;top:208px;width:140px;height:41px">CONTACT ME</div>
    <div class="hero-dots"><i></i><i class="on"></i><i></i></div>
  </div>
</section>

<section class="who">
  <h2 class="heading abs" style="left:85px;top:690px">WHO I AM</h2>
  <p class="body-text abs" style="left:85px;top:740px;width:450px">Sed ut perspiciatis unde omnis iste natus error sit voluptatem accusantium dolorem que laudantium, totam rem aperiam, eaque ipsa quae ab illo inventore veritatis et qu asi architecto beatae vitae dicta sunt explicabo. Nemo enim ipsam voluptatem quia voluptas sit aspernatur aut odit aut fugit, sed quia consequuntur magni dolores eos qui ratione voluptatem sequi nesciunt.</p>
  <p class="body-text abs" style="left:85px;top:890px;width:450px">Sed ut perspiciatis unde omnis iste natus error sit voluptatem accusantium dolorem que laudantium, totam rem aperiam, eaque ipsa quae ab illo inventore veritatis et qu asi architecto beatae vitae dicta sunt explicabo.</p>
  <div class="btn" style="left:85px;top:988px;width:130px;height:42px;font-size:14px">WATCH VIDEO</div>
  <div class="video" role="img" aria-label="Video: a family having a picnic on the beach">
    <div class="video-bar">
      <svg width="9" height="10" viewBox="0 0 9 10"><path d="M0 0L9 5L0 10Z" fill="#ddd"/></svg>
      <span>0:00 / 3:00</span>
    </div>
  </div>
</section>

<section class="services">
  <h2 class="heading center abs" style="left:0;top:35px;width:1200px">OUR SERVICES</h2>
  <p class="body-text center abs" style="left:0;top:75px;width:1200px">Sed ut perspiciatis unde omnis iste natus error sit voluptatem accusantium dolorem que laudantium, totam rem aperiam,</p>
  <div class="service" style="left:85px">
    <div class="service-photo" role="img" aria-label="Photo: a man doing sit-ups on a gym floor" style="background:linear-gradient(135deg,#cfd2d2,#7e8584)"></div>
    <div class="service-title">EXERCISE</div>
    <p class="service-copy">Sed ut perspiciatis unde omnis iste natus error sit voluptatem accusantium doloremque beatae vitae dicta sunt explicabo.</p>
  </div>
  <div class="service" style="left:345px">
    <div class="service-photo" role="img" aria-label="Photo: a father and son cycling outdoors" style="background:linear-gradient(135deg,#e6e2b4,#8fa55e)"></div>
    <div class="service-title">COACHING POINTS</div>
    <p class="service-copy">Sed ut perspiciatis unde omnis iste natus error sit voluptatem accusantium doloremque beatae vitae dicta sunt explicabo.</p>
  </div>
  <div class="service" style="left:605px">
    <div class="service-photo" role="img" aria-label="Photo: a child peeling vegetables in a kitchen" style="background:linear-gradient(135deg,#b8b3ac,#5f6d56)"></div>
    <div class="service-title">SAFETY</div>
    <p class="service-copy">Sed ut perspiciatis unde omnis iste natus error sit voluptatem accusantium doloremque beatae vitae dicta sunt explicabo.</p>
  </div>
  <div class="service" style="left:864px">
    <div class="service-photo" role="img" aria-label="Photo: a man holding a paddle board on the beach" style="background:linear-gradient(180deg,#9cc7e6,#6fa9cf 55%,#d9cdb3 100%)"></div>
    <div class="service-title">SESSION GOAL</div>
    <p class="service-copy">Sed ut perspiciatis unde omnis iste natus error sit voluptatem accusantium doloremque beatae vitae dicta sunt explicabo.</p>
  </div>
</section>

<section class="why" role="img" aria-label="Faint background photo: a father carrying his child on the beach">
  <h2 class="center abs" style="left:0;top:38px;width:1200px;font-family:'Montserrat',Arial,sans-serif;font-weight:500;font-size:25px;letter-spacing:.5px">WHY CHOOSE US</h2>
  <p class="center abs" style="left:0;top:85px;width:1200px;font-size:11.5px">Sed ut perspiciatis unde omnis iste natus error sit voluptatem accusantium dolorem que &nbsp;laudantium, totam rem aperiam</p>
  <svg class="abs" style="left:35px;top:210px" width="20" height="100" viewBox="0 0 20 100"><path d="M18 0L2 50L18 100" fill="none" stroke="rgba(255,255,255,.6)" stroke-width="1.5"/></svg>
  <svg class="abs" style="left:1145px;top:210px" width="20" height="100" viewBox="0 0 20 100"><path d="M2 0L18 50L2 100" fill="none" stroke="rgba(255,255,255,.6)" stroke-width="1.5"/></svg>

  <div class="pillar" style="left:78px">
    <div class="pillar-ring"><svg width="52" height="52" viewBox="0 0 52 52" fill="none" stroke="#fff" stroke-width="3"><path d="M26 16C18 10 8 14 9 27C10 40 18 48 26 44C34 48 42 40 43 27C44 14 34 10 26 16Z"/><path d="M26 16C26 10 29 6 33 5"/></svg></div>
    <div class="pillar-label">NUTRITION</div>
  </div>
  <div class="pillar" style="left:284px">
    <div class="pillar-ring"><svg width="56" height="56" viewBox="0 0 56 56" fill="none" stroke="#fff" stroke-width="4" stroke-linecap="round"><circle cx="34" cy="9" r="4" fill="#fff" stroke="none"/><path d="M30 18L22 32L32 38L28 50"/><path d="M22 32L14 44"/><path d="M30 18L40 26L48 24"/><path d="M30 18L20 20L14 28"/><path d="M4 24H12M2 32H10M4 40H10" stroke-width="2.5"/></svg></div>
    <div class="pillar-label">EXERCISE</div>
  </div>
  <div class="pillar" style="left:490px">
    <div class="pillar-ring"><svg width="56" height="56" viewBox="0 0 56 56" fill="none" stroke="#fff" stroke-width="3"><path d="M28 16C20 16 15 22 15 29C15 38 28 48 28 48C28 48 41 38 41 29C41 22 36 16 28 16Z" fill="#fff"/><circle cx="28" cy="29" r="5" fill="#14a99a" stroke="none"/><path d="M28 4V10M14 8L17 13M42 8L39 13M6 18L11 20M50 18L45 20" stroke-width="2.5" stroke-linecap="round"/></svg></div>
    <div class="pillar-label">MENTAL WELL<br>BEING</div>
  </div>
  <div class="pillar" style="left:696px">
    <div class="pillar-ring"><svg width="56" height="56" viewBox="0 0 56 56" fill="#fff"><rect x="6" y="26" width="4" height="20"/><rect x="10" y="34" width="40" height="6"/><rect x="46" y="34" width="4" height="12"/><rect x="22" y="28" width="24" height="6" rx="2"/><circle cx="16" cy="30" r="4"/><text x="30" y="22" font-family="Montserrat,Arial,sans-serif" font-weight="700" font-size="10">z</text><text x="36" y="16" font-family="Montserrat,Arial,sans-serif" font-weight="700" font-size="10">z</text><text x="42" y="10" font-family="Montserrat,Arial,sans-serif" font-weight="700" font-size="10">z</text></svg></div>
    <div class="pillar-label">SLEEP<br>ADEQUATE/QUALITY</div>
  </div>
  <div class="pillar" style="left:901px">
    <div class="pillar-ring"><svg width="56" height="56" viewBox="0 0 56 56" fill="#fff"><circle cx="28" cy="12" r="6"/><path d="M20 20H36L38 34L46 40L44 43L34 38H22L12 43L10 40L18 34Z"/><path d="M8 44C16 40 22 46 28 46C34 46 40 40 48 44L46 48H10Z"/></svg></div>
    <div class="pillar-label">PLAY<br>REST &amp; RECUPERATION</div>
  </div>
</section>

<section class="testimonials">
  <h2 class="heading center abs" style="left:0;top:2033px;width:1200px">OUR TESTIMONIALS</h2>
  <p class="body-text center abs" style="left:0;top:2073px;width:1200px">Sed ut perspiciatis unde omnis iste natus error sit voluptatem accusantium dolorem que laudantium, totam rem aperiam,</p>
  <svg class="abs" style="left:40px;top:2150px" width="20" height="110" viewBox="0 0 20 110"><path d="M18 0L2 55L18 110" fill="none" stroke="#e2e2e2" stroke-width="1.5"/></svg>
  <svg class="abs" style="left:1140px;top:2150px" width="20" height="110" viewBox="0 0 20 110"><path d="M2 0L18 55L2 110" fill="none" stroke="#e2e2e2" stroke-width="1.5"/></svg>

  <div class="testimonial" style="left:86px">
    <div class="avatar" role="img" aria-label="Portrait photo of a client"></div>
    <p class="quote"><b>"</b>Sed ut perspiciatis unde omnis iste natus error sit voluptatem accusantium doloremque laudantium, totam rem vitae dicta sunt explicabo.</p>
    <div class="t-name">JHON SMITH</div>
    <div class="t-date">POSTED ON 25 JUNE 2017</div>
    <svg class="t-stars" width="64" height="12" viewBox="0 0 64 12"><g fill="none" stroke="#f2b01e" stroke-width="1"><path id="s1" d="M6 1L7.5 4.5L11 4.8L8.3 7.1L9.1 10.6L6 8.8L2.9 10.6L3.7 7.1L1 4.8L4.5 4.5Z"/><use href="#s1" x="13"/><use href="#s1" x="26"/><use href="#s1" x="39"/></g><path d="M58 1L59.5 4.5L63 4.8L60.3 7.1L61.1 10.6L58 8.8L54.9 10.6L55.7 7.1L53 4.8L56.5 4.5Z" fill="#f2b01e"/></svg>
  </div>
  <div class="testimonial" style="left:436px">
    <div class="avatar" role="img" aria-label="Portrait photo of a client"></div>
    <p class="quote"><b>"</b>Sed ut perspiciatis unde omnis iste natus error sit voluptatem accusantium doloremque laudantium, totam rem vitae dicta sunt explicabo.</p>
    <div class="t-name">JHON SMITH</div>
    <div class="t-date">POSTED ON 25 JUNE 2017</div>
    <svg class="t-stars" width="64" height="12" viewBox="0 0 64 12"><g fill="none" stroke="#f2b01e" stroke-width="1"><use href="#s1"/><use href="#s1" x="13"/><use href="#s1" x="26"/><use href="#s1" x="39"/></g><path d="M58 1L59.5 4.5L63 4.8L60.3 7.1L61.1 10.6L58 8.8L54.9 10.6L55.7 7.1L53 4.8L56.5 4.5Z" fill="#f2b01e"/></svg>
  </div>
  <div class="testimonial" style="left:786px">
    <div class="avatar" role="img" aria-label="Portrait photo of a client"></div>
    <p class="quote"><b>"</b>Sed ut perspiciatis unde omnis iste natus error sit voluptatem accusantium doloremque laudantium, totam rem vitae dicta sunt explicabo.</p>
    <div class="t-name">JHON SMITH</div>
    <div class="t-date">POSTED ON 25 JUNE 2017</div>
    <svg class="t-stars" width="64" height="12" viewBox="0 0 64 12"><g fill="none" stroke="#f2b01e" stroke-width="1"><use href="#s1"/><use href="#s1" x="13"/><use href="#s1" x="26"/><use href="#s1" x="39"/></g><path d="M58 1L59.5 4.5L63 4.8L60.3 7.1L61.1 10.6L58 8.8L54.9 10.6L55.7 7.1L53 4.8L56.5 4.5Z" fill="#f2b01e"/></svg>
  </div>
</section>

<footer class="site-footer">
  <div class="foot-brand">
    <div class="foot-brand-name"><span class="foot-brand-square"></span>ROB CALDER</div>
    <div class="foot-brand-sub">HEALTH COACH</div>
  </div>

  <div class="foot-heading" style="left:383px">CONTACT US</div>
  <div class="contact-row" style="top:92px">
    <svg width="14" height="13" viewBox="0 0 14 13" fill="#fff"><path d="M1 4C1 2 3 1 7 1S13 2 13 4V5H10V3.5H4V5H1Z"/><rect x="2" y="6" width="10" height="6" rx="1"/></svg>
    <span>(000)-121-1231 &nbsp;(Phone)</span>
  </div>
  <div class="contact-row" style="top:120px">
    <svg width="14" height="13" viewBox="0 0 14 13" fill="#fff"><rect x="3" y="0" width="8" height="4"/><rect x="0" y="4" width="14" height="6" rx="1"/><rect x="3" y="8" width="8" height="5" fill="#fff" stroke="#231f20"/></svg>
    <span>(000)-121-1231 &nbsp;(Fax)</span>
  </div>
  <div class="contact-row" style="top:149px">
    <svg width="14" height="11" viewBox="0 0 14 11"><rect x="0" y="0" width="14" height="11" fill="#fff"/><path d="M0 0L7 6L14 0" fill="none" stroke="#231f20" stroke-width="1.2"/></svg>
    <span style="text-decoration:underline">hello@calderhealthcoach.co.uk</span>
  </div>
  <div class="contact-row" style="top:176px">
    <svg width="14" height="16" viewBox="0 0 14 16" fill="#fff"><path d="M7 0C3 0 1 3 1 6C1 10 7 16 7 16S13 10 13 6C13 3 11 0 7 0Z"/><circle cx="7" cy="6" r="2.3" fill="#231f20"/></svg>
    <span>P.O. Box 760Lorem Ipsum Dummy<br>Lorem Ipsum Dummy</span>
  </div>

  <div class="foot-heading" style="left:651px">NEWSLETTER</div>
  <p class="foot-text" style="left:651px;top:86px;width:240px">Register Your email address to get information ablout us</p>
  <div class="email-field">Email Address</div>
  <div class="btn" style="left:651px;top:181px;width:82px;height:25px;font-size:10px;font-family:'Arimo',Arial,sans-serif;font-weight:700">SUBSCRIBE</div>

  <div class="foot-heading" style="left:921px;top:46px">FOLLOW US</div>
  <p class="foot-text" style="left:921px;top:88px;width:200px;font-size:11.5px">Lorem ipsum dolor sit amet, conse ctetur adipiscing elit. Nulla in purus nibh. Donec ornare</p>
  <div class="social">
    <div class="social-item"><span class="social-dot"></span>Circlebook</div>
    <div class="social-item"><span class="social-dot"></span>ProLinks</div>
  </div>

  <div class="abs" style="left:383px;top:242px;width:732px;height:1px;background:var(--rule)"></div>
  <p class="abs center" style="left:0;top:269px;width:1200px;font-size:12px">© Copyright 2017 Men's Health Coaching Business.All Rights Reserved</p>
</footer>

</body>
</html>
```